standardize print collateral

we need help standardizing all print collateral and website. top priorities:

1. standardized case studies template
2. standardized marketing slicks template
3. standardized powerpoint template
Updates

Project Deadline Extended
Reason: We are extending the project to allow current design submissions to be tweaked while providing the opportunity for new designs to be submitted. We will need all 3 collateral designs submitted to make a final decision. Please note, these 3 designs should all look different, needless to say they should all compliment eachother. As for some direction, the powerpoint main color should not be yellow since yellow does not show up the same shade on any screen. The case study and marketing slicks will be printed and often sit next to our competitors marketing material - think high end product, technology, revolutionary, edgy, professional. The designs should compliment eachother and feel like the Brightfern Metrics brand (which you are determining) and should stand out professionally. We are open to introducing new colors into our brand, the only thing that must remain the same is our logo. Have fun, make it edgy, and keep it professional. Looking forward to seeing what you submit!

Target Market(s)

Property Casualty Insurance Companies: Executive level wording with actuarial credibility

Industry/Entity Type

Marketing

Requirements
Must have
• professional layout for existing collateral and 2-page marketing slicks. style guide/colors can be transferred to powerpoint. logo must stay; everything else (i.e. color, font, layout/structure etc.) is flexible. The three components should not looks the same, they should only compliment eachother.
Nice to have
• we are revolutionizing a conservative industry, so adequate level of edgy/advanced technology/impactful feel to layout
Should not have
• no need to stay within color constraints of yellow, but need to appropriately work well with the eagle head logo

```html
<!DOCTYPE html>
<html lang="en">
<head>
<meta charset="utf-8">
<title>Rapid Portfolio Analysis – Brightfern Metrics</title>
<link href="https://fonts.googleapis.com/css2?family=Roboto+Condensed:wght@300;400;700&display=swap" rel="stylesheet">
<style>
:root{
  --gold:#e9a51e;
  --teal:#0f6d6a;
  --teal-dark:#0b5653;
  --ink:#2b2b2b;
  --white:#ffffff;
  --grid:#c9c9c9;
  --head-fill:#f3f1e6;
  --good:#6fbf5f;
  --warn:#f1c24c;
  --bad:#e0644f;
}
*{margin:0;padding:0;box-sizing:border-box}
html,body{width:927px;height:1200px;overflow:hidden;background:var(--white)}
body{font-family:"Roboto Condensed",sans-serif;color:var(--ink);position:relative}
.sheet{position:relative;width:927px;height:1200px;overflow:hidden}

.title{position:absolute;top:38px;left:0;width:100%;text-align:center;color:var(--gold);font-weight:700;font-size:46px;letter-spacing:.2px}
.subtitle{position:absolute;top:98px;left:0;width:100%;text-align:center;font-size:21px;font-weight:400}
.intro{position:absolute;top:140px;left:61px;width:810px;font-size:15px;line-height:20px;text-align:justify}

.how-band{position:absolute;top:261px;left:0;width:927px;height:429px;background:var(--teal)}
.how-tab{position:absolute;top:278px;left:0;width:320px;height:58px;background:var(--white);clip-path:polygon(0 0,100% 0,92% 100%,0 100%)}
.how-heading{position:absolute;top:288px;left:22px;font-size:31px;color:var(--teal);font-weight:300;letter-spacing:.3px}
.how-heading b{font-weight:700}
.how-heading .mark{color:var(--gold);font-weight:700}

.step{position:absolute;left:61px;width:810px;color:var(--white)}
.step-title{font-size:27px;font-weight:700;text-transform:uppercase;letter-spacing:.2px}
.step-title span{font-size:21px;font-weight:400;text-transform:none}
.step-body{margin:4px 0 0 30px;font-size:15.5px;line-height:20px;font-weight:300}

.panel-title{position:absolute;font-size:21px;color:var(--teal);font-weight:300;text-align:center}
.panel-title b{font-weight:700}
.panel-text{position:absolute;font-size:15.5px;line-height:20px;text-align:center}

.portfolio-title{top:733px;left:110px;width:400px}
.portfolio-text{top:762px;left:110px;width:400px}

.score-table{position:absolute;top:812px;left:61px;width:404px;border-collapse:collapse;font-size:7.4px;line-height:1.1}
.score-table th,.score-table td{border:1px solid var(--grid);padding:2px 2px;text-align:right;white-space:nowrap}
.score-table th{background:var(--head-fill);font-weight:700;text-align:center;white-space:normal;vertical-align:bottom}
.score-table td:first-child{text-align:left}
.score-table .good{background:var(--good)}
.score-table .warn{background:var(--warn)}
.score-table .bad{background:var(--bad)}
.score-table .total td{font-weight:700}

.dashboard{position:absolute;top:707px;left:474px;width:374px;height:161px;border:2px solid var(--gold);background:linear-gradient(180deg,#dfe7ea 0%,#c7d9c8 45%,#e8c9b6 100%)}

.distribution-title{top:888px;left:474px;width:380px}
.distribution-text{top:918px;left:474px;width:380px}

.report-band{position:absolute;top:1126px;left:0;width:927px;height:74px;background:var(--teal);color:var(--white);text-align:center}
.report-heading{margin-top:6px;font-size:17px;font-weight:400}
.report-body{margin:2px auto 0;width:860px;font-size:13.2px;line-height:15px;font-weight:300}
</style>
</head>
<body>
<main class="sheet">
  <h1 class="title">Rapid Portfolio Analysis</h1>
  <p class="subtitle">Winning Against Adverse Selection</p>
  <p class="intro">The property and casualty market is over-supplied with excess capacity, and current pricing methods are inconsistent and outdated. This leads to a considerable level of adverse selection within nearly every portfolio. Almost every insurer is attracting customers who are underpriced and losing business where they are overpriced. This invisible effect only surfaces after evidence of slowly deteriorating portfolio loss ratios, resulting in premium increases across the portfolio. These across-the-board premium increases exacerbate the problem by overpricing the most profitable customers and driving them into the arms of competitors.</p>

  <section class="how-band" aria-hidden="false"></section>
  <div class="how-tab"></div>
  <h2 class="how-heading"><b>HOW</b> DOES IT WORK<span class="mark">?</span></h2>

  <div class="step" style="top:346px">
    <h3 class="step-title">Detection: <span>is the portfolio priced correctly?</span></h3>
    <p class="step-body">Veridex employs a regression method based on a technological breakthrough. It exposes pricing imbalances by commonly employed rating methods including the GLM. These pricing imbalances are the major drivers of adverse selection.</p>
  </div>
  <div class="step" style="top:443px">
    <h3 class="step-title">Measurement: <span>how is the portfolio trending?</span></h3>
    <p class="step-body">Veridex scores the two most important attributes of the portfolio: the adequacy of rates and the quality of the business on a progressive basis. In addition, Veridex projects the financial outcome of business as it is written with startling accuracy. Insurers are able to know significantly in advance of trends in their business.</p>
  </div>
  <div class="step" style="top:580px">
    <h3 class="step-title">Correction: <span>how to address the issues?</span></h3>
    <p class="step-body">Veridex provides an array of options for addressing any deterioration in the portfolio. These options range from specifically designed rate adjustments and underwriting strategies, to simple distribution management sales and profitability strategies.</p>
  </div>

  <h2 class="panel-title portfolio-title"><b>PORTFOLIO</b> MONITORING</h2>
  <p class="panel-text portfolio-text">Predict the future loss ratio of the business<br>being written - both renewals and new business</p>

  <table class="score-table">
    <thead>
      <tr><th>Policy Effective Period</th><th>Earned Exposure</th><th>Earned Premium</th><th>Losses</th><th>Claims</th><th>Loss Ratio</th><th>Rate Level</th><th>Portfolio Score</th><th>Good Percent Exposure</th><th>Average Percent Exposure</th><th>Poor Percent Exposure</th></tr>
    </thead>
    <tbody>
      <tr><td>2001/Q1</td><td>15,900</td><td>$11,918,029</td><td>$5,943,289</td><td>462</td><td>78.57%</td><td class="bad">0.968</td><td class="warn">523</td><td>35.51%</td><td>41.86%</td><td>22.63%</td></tr>
      <tr><td>2001/Q2</td><td>41,828</td><td>$14,425,434</td><td>$6,216,889</td><td>575</td><td>43.10%</td><td class="bad">0.959</td><td class="warn">532</td><td>38.59%</td><td>40.11%</td><td>20.59%</td></tr>
      <tr><td>2001/Q3</td><td>43,883</td><td>$14,217,491</td><td>$9,396,107</td><td>486</td><td>65.63%</td><td class="bad">0.962</td><td class="warn">505</td><td>36.70%</td><td>39.17%</td><td>22.13%</td></tr>
      <tr><td>2001/Q4</td><td>37,145</td><td>$13,590,795</td><td>$6,357,470</td><td>408</td><td>46.78%</td><td class="warn">0.97</td><td class="warn">524</td><td>36.83%</td><td>40.75%</td><td>22.42%</td></tr>
      <tr><td>2007/Q1</td><td>37,969</td><td>$21,200,710</td><td>$9,342,857</td><td>359</td><td>44.07%</td><td class="good">1.049</td><td class="good">495</td><td>31.81%</td><td>35.59%</td><td>22.60%</td></tr>
      <tr><td>2007/Q2</td><td>47,247</td><td>$23,960,971</td><td>$7,413,445</td><td>490</td><td>30.97%</td><td class="good">1.042</td><td class="good">502</td><td>33.42%</td><td>39.89%</td><td>26.90%</td></tr>
      <tr><td>2007/Q3</td><td>40,984</td><td>$20,470,545</td><td>$8,206,414</td><td>383</td><td>40.09%</td><td class="good">1.056</td><td class="good">501</td><td>33.48%</td><td>35.73%</td><td>30.79%</td></tr>
      <tr><td>2007/Q4</td><td>36,534</td><td>$23,383,720</td><td>$10,884,148</td><td>491</td><td>45.28%</td><td class="good">1.078</td><td class="bad">492</td><td>31.32%</td><td>34.81%</td><td>33.87%</td></tr>
      <tr><td>2008/Q1</td><td>40,671</td><td>$21,959,902</td><td>$7,190,574</td><td>371</td><td>32.74%</td><td class="good">1.073</td><td class="bad">491</td><td>31.15%</td><td>34.21%</td><td>34.64%</td></tr>
      <tr><td>2008/Q2</td><td>47,291</td><td>$24,645,178</td><td>$9,865,707</td><td>424</td><td>40.03%</td><td class="good">1.055</td><td class="good">501</td><td>33.11%</td><td>35.83%</td><td>31.09%</td></tr>
      <tr><td>2008/Q3</td><td>36,289</td><td>$16,831,701</td><td>$4,134,601</td><td>321</td><td>21.86%</td><td class="good">1.058</td><td class="good">497</td><td>32.69%</td><td>34.89%</td><td>32.46%</td></tr>
      <tr><td>2008/Q4</td><td>31,858</td><td>$17,186,276</td><td>$4,128,558</td><td>284</td><td>24.03%</td><td class="good">1.073</td><td class="bad">485</td><td>30.50%</td><td>34.50%</td><td>35.21%</td></tr>
      <tr class="total"><td>Total</td><td>1,211,762</td><td>$595,065,403</td><td>$232,595,818</td><td>12,988</td><td>39.09%</td><td>1</td><td>520</td><td>36.93%</td><td>39.76%</td><td>24.31%</td></tr>
      <tr><td colspan="8">Average Loss Ratio:</td><td>26%</td><td>40%</td><td>53%</td></tr>
    </tbody>
  </table>

  <div class="dashboard" role="img" aria-label="Distribution dashboard screen listing agents with colour-coded score bars"></div>

  <h2 class="panel-title distribution-title"><b>DISTRIBUTION</b> MONITORING</h2>
  <p class="panel-text distribution-text">Constantly track the quality and performance<br>of individual distribution outlets based on the<br>underwriting score of each policy</p>

  <footer class="report-band">
    <h2 class="report-heading">Let Brightfern Metrics Build Your Portfolio Analysis Report</h2>
    <p class="report-body">The report details your portfolio trends and identifies future unseen problems before they occur. The insight provided in the report exhibits what is actually going on in your portfolio. This likely includes adverse selection, impact of price changes with unintended consequences, and the emerging trends in the composition of the book. The analysis results not only reveal past trends, but also predict future impact.</p>
  </footer>
</main>
</body>
</html>
```